Business card design and logo for hot water plumbing business

I need a logo and business card for my business which installs hot water heaters
Must have on front:
Paramount Hot Water Services
Gareth Pellow
0498163204

Either front or back:
gareth@paramounthotwaterservices-example.com.au
ABN 48207153690
Licence No 538412K

On the back in point form:
Supply and installation of
• electric storage
• gas storage/instantaneous
• heat pumps
• solar heaters

Iv provided 3 examples of cards I like but open to different ideas.

```html
<!DOCTYPE html>
<html lang="en">
<head>
<meta charset="utf-8">
<title>Paramount Hot Water Services – Business Card</title>
<link rel="stylesheet" href="https://fonts.googleapis.com/css2?family=Roboto:wght@400;500;700&display=swap">
<style>
  :root {
    --blue-deep: #1670c9;
    --blue-mid: #2a8fe2;
    --blue-light: #5bb8f5;
    --brand-blue: #1a6fc4;
    --orange: #f0562a;
    --yellow: #f7b21c;
    --white: #ffffff;
    --grey: #8a939c;
    --backdrop: #e9ecef;
  }
  * { box-sizing: border-box; margin: 0; padding: 0; }
  html, body { width: 1200px; height: 855px; overflow: hidden; }
  body {
    position: relative;
    background: var(--backdrop);
    font-family: "Roboto", Arial, sans-serif;
  }
  .card {
    position: absolute;
    width: 520px;
    height: 300px;
    border-radius: 22px;
    overflow: hidden;
    box-shadow: 0 10px 28px rgba(0,0,0,.22);
  }
  .card svg { position: absolute; inset: 0; }
  .card-back { left: 50px; top: 230px; }
  .card-front { left: 630px; top: 230px; }

  .wordmark { position: absolute; display: flex; align-items: center; gap: 12px; font-weight: 700; line-height: 1; }
  .wordmark .dot { border-radius: 50%; flex: none; }
  .wordmark .name-main { display: block; letter-spacing: .5px; }
  .wordmark .name-sub { display: block; letter-spacing: 1px; margin-top: 4px; }

  .card-back .wordmark { left: 70px; top: 118px; color: var(--white); }
  .card-back .dot { width: 30px; height: 30px; background: var(--white); }
  .card-back .name-main { font-size: 46px; }
  .card-back .name-sub { font-size: 19px; }

  .card-front .wordmark { left: 170px; top: 26px; color: var(--brand-blue); }
  .card-front .dot { width: 22px; height: 22px; background: var(--brand-blue); }
  .card-front .name-main { font-size: 34px; }
  .card-front .name-sub { font-size: 14px; }

  .registration { position: absolute; left: 22px; top: 92px; color: var(--grey); font-size: 11px; line-height: 1.5; }
  .holder-name { position: absolute; left: 36px; top: 182px; color: var(--white); font-size: 27px; font-weight: 700; }
  .contact-list { position: absolute; left: 36px; top: 228px; list-style: none; color: var(--white); font-size: 12.5px; }
  .contact-list li { display: flex; align-items: center; gap: 8px; margin-bottom: 8px; }
  .contact-list svg { position: static; flex: none; }
  .service-list { position: absolute; left: 318px; top: 118px; list-style: none; color: var(--white); font-size: 13px; text-transform: uppercase; }
  .service-list li { margin-bottom: 10px; padding-left: 12px; position: relative; }
  .service-list li::before { content: ""; position: absolute; left: 0; top: 5px; width: 5px; height: 5px; border-radius: 50%; background: var(--yellow); }

  .brand-sign { right: 36px; bottom: 28px; color: var(--brand-blue); }
  .brand-sign .dot { width: 26px; height: 26px; background: var(--brand-blue); }
  .brand-sign .name-main { font-size: 44px; }
  .brand-sign .name-sub { font-size: 18px; }
</style>
</head>
<body>

<section class="card card-back" aria-label="Card back">
  <svg width="520" height="300" viewBox="0 0 520 300">
    <defs>
      <linearGradient id="backFill" x1="0" y1="1" x2="1" y2="0">
        <stop offset="0" stop-color="var(--blue-deep)"/>
        <stop offset="1" stop-color="var(--blue-mid)"/>
      </linearGradient>
    </defs>
    <rect width="520" height="300" fill="url(#backFill)"/>
    <path d="M300 0 C370 8 430 70 520 80 L520 0 Z" fill="var(--blue-light)"/>
    <path d="M300 0 C370 8 430 70 520 80" fill="none" stroke="var(--orange)" stroke-width="9"/>
    <path d="M292 8 C365 20 425 82 520 94" fill="none" stroke="var(--yellow)" stroke-width="6"/>
  </svg>
  <div class="wordmark">
    <span class="dot"></span>
    <span><span class="name-main">PARAMOUNT</span><span class="name-sub">HOT WATER SERVICES</span></span>
  </div>
</section>

<section class="card card-front" aria-label="Card front">
  <svg width="520" height="300" viewBox="0 0 520 300">
    <defs>
      <linearGradient id="frontFill" x1="0" y1="1" x2="1" y2="0">
        <stop offset="0" stop-color="var(--blue-deep)"/>
        <stop offset="1" stop-color="var(--blue-mid)"/>
      </linearGradient>
    </defs>
    <rect width="520" height="300" fill="var(--white)"/>
    <path d="M0 168 C150 120 340 95 520 62 L520 300 L0 300 Z" fill="url(#frontFill)"/>
    <path d="M0 162 C150 114 340 89 520 56" fill="none" stroke="var(--yellow)" stroke-width="5"/>
    <path d="M0 167 C150 119 340 94 520 61" fill="none" stroke="var(--orange)" stroke-width="4"/>
  </svg>
  <div class="wordmark">
    <span class="dot"></span>
    <span><span class="name-main">PARAMOUNT</span><span class="name-sub">HOT WATER SERVICES</span></span>
  </div>
  <p class="registration">ABN 48207153690<br>Licence No 538412K</p>
  <h1 class="holder-name">Gareth Pellow</h1>
  <ul class="contact-list">
    <li>
      <svg width="12" height="12" viewBox="0 0 12 12" aria-hidden="true"><rect width="12" height="12" rx="3" fill="var(--yellow)"/><path d="M4 3h1.5l.5 2-1 .7a4 4 0 0 0 1.8 1.8l.7-1 2 .5V8.5A1 1 0 0 1 8.5 9.5 6 6 0 0 1 3 4a1 1 0 0 1 1-1z" fill="var(--white)"/></svg>
      0498163204
    </li>
    <li>
      <svg width="12" height="12" viewBox="0 0 12 12" aria-hidden="true"><rect width="12" height="12" rx="3" fill="var(--yellow)"/><rect x="2.5" y="3.5" width="7" height="5" fill="none" stroke="var(--white)"/><path d="M2.5 3.5 6 6.5 9.5 3.5" fill="none" stroke="var(--white)"/></svg>
      gareth@paramounthotwaterservices-example.com.au
    </li>
  </ul>
  <ul class="service-list">
    <li>Heat pumps</li>
    <li>Solar heaters</li>
    <li>Electric storage</li>
    <li>Gas storage/instantaneous</li>
  </ul>
</section>

<div class="wordmark brand-sign">
  <span class="dot"></span>
  <span><span class="name-main">PARAMOUNT</span><span class="name-sub">HOT WATER SERVICES</span></span>
</div>

</body>
</html>
```